Stabilization Flyer

We are looking for a single document that outlines the info below - we want to emphasize that we can help child cares in the process and then we can help them make any award money go further through our program -
Don’t leave money on the table – as a child care owner you have access to grant money, but time is running out.

President Halvorsen signed the National Renewal Fund Act of 2021 (NRF). This plan includes $24 billion in child care stabilization grant funding. These funds will help keep early childhood educators and family child care providers keep their doors open and provide a critical step to paving the way for a strong economic recovery and a more equitable future.

Each State has its own application process – most licensed child care centers are eligible for grants with awards up to $400,000 per program. Awarded dollars is based upon your center’s capacity.

Grants are good for the following categories

Child care providers can use stabilization subgrants to cover these expenses:
• Wages and benefits, including increases in compensation for any staff.
• Rent, utilities, facilities maintenance and minor renovations, and insurance.
• Personal protective equipment, cleaning supplies, and other health and safety measures.
• Equipment and supplies used to respond to COVID-19.
• Material goods (i.e., to facilitate play or safe sleep) or services (i.e., food) used for the operation of the program. Yes, Food is an allowable expense.
• Mental health services for children and employees

If you have not applied for the grant, we can help point you in the right direction. Just email stablization@pantryandgoodsdepot.com or call 877. 391.6052 and we will send you the links on how to file within your State. No purchase is necessary for this guidance, but we would love the opportunity to show you how we can stretch your purchases by up to 30%.

Target Market(s)

child care centers

Industry/Entity Type

child care is the target

Requirements
Must have
• website www.pantryandgoodsdepot.com
Nice to have
• we have a video that could be embedded https://www.pantryandgoodsdepot.com/video-resources/

```html
<!DOCTYPE html>
<html lang="en">
<head>
<meta charset="utf-8">
<title>Stabilization Flyer</title>
<link href="https://fonts.googleapis.com/css2?family=Oswald:wght@500&family=Open+Sans:wght@400;600;700&display=swap" rel="stylesheet">
<style>
  :root {
    --blue: #3b7fd0;
    --green: #8ec97c;
    --green-dark: #5fae54;
    --ink: #4a4b4d;
    --ink-soft: #6b6c6e;
    --paper: #ffffff;
    --page-bg: #eceef1;
  }
  * { box-sizing: border-box; margin: 0; padding: 0; }
  html, body { width: 956px; height: 1200px; overflow: hidden; background: var(--page-bg); }
  body { font-family: "Open Sans", Arial, sans-serif; color: var(--ink); }
  .flyer { position: relative; width: 956px; height: 1200px; background: var(--paper); overflow: hidden; }

  .brand { position: absolute; left: 54px; top: 52px; display: flex; align-items: center; gap: 10px; }
  .brand-mark { width: 30px; height: 30px; background: var(--green); }
  .brand-name { font-size: 26px; font-weight: 600; color: var(--ink); line-height: 1; }
  .brand-tagline { position: absolute; left: 54px; top: 94px; font-size: 11px; color: var(--ink-soft); white-space: nowrap; letter-spacing: .5px; text-transform: uppercase; }

  .hero-photo { position: absolute; right: 0; top: 0; width: 418px; height: 372px;
    background: linear-gradient(135deg, #e9ddd6 0%, #c9b3a8 45%, #8f7f78 75%, #d8d1cc 100%); }

  .kicker { position: absolute; left: 54px; top: 158px; font-size: 24px; font-weight: 700; color: var(--blue); letter-spacing: .3px; }
  .title { position: absolute; left: 52px; top: 178px; font-family: "Oswald", "Arial Narrow", sans-serif; font-weight: 500;
    font-size: 64px; line-height: 72px; color: var(--ink); letter-spacing: 1px; }
  .act-band { position: absolute; left: 0; top: 328px; width: 540px; height: 44px; background: var(--blue);
    color: #fff; font-weight: 700; font-size: 32px; line-height: 44px; padding-left: 70px; letter-spacing: 1px; }

  .intro { position: absolute; left: 56px; top: 390px; width: 416px; font-size: 15px; line-height: 19px; }
  .intro strong, .accent { color: var(--blue); font-weight: 700; }
  .state-heading { position: absolute; left: 54px; top: 522px; font-size: 20px; font-weight: 600; line-height: 25px; }
  .state-rule { position: absolute; left: 256px; top: 560px; width: 212px; border-top: 1px solid var(--green); }
  .state-rule::before { content: ""; position: absolute; left: -3px; top: -3px; width: 5px; height: 5px; border-radius: 50%; background: var(--green); }
  .state-note { position: absolute; left: 54px; top: 580px; width: 420px; font-size: 13px; line-height: 18px; color: var(--ink-soft); }
  .state-note b { color: var(--ink); }

  .child-photo { position: absolute; left: 0; top: 650px; width: 360px; height: 550px;
    background: linear-gradient(160deg, #f4f2f0 0%, #e6dcd4 40%, #e8a8a3 70%, #d94a4a 100%); }

  .uses-heading { position: absolute; left: 497px; top: 392px; width: 350px; font-size: 20px; font-weight: 600; line-height: 25px; }
  .uses-list { position: absolute; left: 497px; top: 498px; width: 400px; list-style: none; }
  .uses-list li { position: relative; padding-left: 44px; font-size: 14px; line-height: 16px; margin-bottom: 14px; }
  .uses-list svg { position: absolute; left: 6px; top: 0; }

  .video-band { position: absolute; left: 445px; top: 826px; width: 511px; height: 92px; background: var(--green); padding: 20px 0 0 52px; }
  .video-title { font-size: 18px; }
  .video-title a { color: var(--blue); text-decoration: none; }
  .video-url { margin-top: 10px; font-size: 13.5px; width: 410px; padding-bottom: 4px; border-bottom: 1px solid var(--ink); }

  .closing { position: absolute; left: 497px; top: 940px; width: 420px; font-size: 14.5px; line-height: 18.5px; }
  .closing p + p { margin-top: 10px; }
  .closing .green { color: var(--green-dark); font-weight: 700; }

  .contact-tab { position: absolute; left: 363px; top: 1082px; width: 180px; height: 28px; background: var(--green);
    border-radius: 14px 14px 0 0; color: #fff; font-weight: 600; font-size: 19px; line-height: 30px; padding-left: 16px; letter-spacing: .5px; }
  .contact-band { position: absolute; left: 360px; top: 1110px; width: 596px; height: 90px; background: var(--blue); color: #fff; }
  .contact-list { position: absolute; left: 22px; top: 8px; list-style: none; }
  .contact-list li { display: flex; align-items: center; gap: 8px; font-size: 13px; line-height: 23px; }
  .contact-list .phone { font-size: 19px; font-weight: 700; line-height: 28px; }
  .follow { position: absolute; right: 52px; top: 18px; text-align: center; font-size: 15px; font-weight: 600; }
  .social { display: flex; gap: 5px; justify-content: center; margin-top: 8px; }
  .social span { width: 19px; height: 19px; border-radius: 50%; background: #fff; }
</style>
</head>
<body>
<main class="flyer">
  <div class="brand">
    <span class="brand-mark"></span>
    <span class="brand-name">Pantry Goods Depot</span>
  </div>
  <p class="brand-tagline">Child Care Supply Partner</p>

  <div class="hero-photo" role="img" aria-label="Photo of a teacher reading a picture book to three young children"></div>

  <p class="kicker">PRESIDENT HALVORSEN SIGNED</p>
  <h1 class="title">THE NATIONAL<br>RENEWAL FUND</h1>
  <div class="act-band">ACT OF 2021 (NRF)</div>

  <p class="intro">This plan includes <strong>$24 billion</strong> in child care stabilization grant funding. These funds will help keep early childhood educators and family child care providers keep their doors open and provide a critical step to paving the way for a strong economic recovery and a more equitable future.</p>

  <h2 class="state-heading">Each State has its own<br>application process</h2>
  <span class="state-rule"></span>
  <p class="state-note">Most licensed child care centers are eligible for grants with awards up to <b>$400,000 per program.</b> Awarded dollars is based upon your center’s capacity.</p>

  <div class="child-photo" role="img" aria-label="Photo of a toddler riding a red bouncing toy deer in a playroom"></div>

  <h2 class="uses-heading">Child care providers can use <span class="accent">stabilization subgrants</span> to cover these expenses:</h2>
  <ul class="uses-list">
    <li><svg width="22" height="22" viewBox="0 0 22 22"><circle cx="11" cy="11" r="10" fill="none" stroke="var(--green)" stroke-width="2"/><path d="M6 11l3.5 3.5L16 8" fill="none" stroke="var(--green)" stroke-width="2.4"/></svg>Wages and benefits, including increases in compensation for any staff.</li>
    <li><svg width="22" height="22" viewBox="0 0 22 22"><circle cx="11" cy="11" r="10" fill="none" stroke="var(--green)" stroke-width="2"/><path d="M6 11l3.5 3.5L16 8" fill="none" stroke="var(--green)" stroke-width="2.4"/></svg>Rent, utilities, facilities maintenance and minor renovations, &amp; insurance.</li>
    <li><svg width="22" height="22" viewBox="0 0 22 22"><circle cx="11" cy="11" r="10" fill="none" stroke="var(--green)" stroke-width="2"/><path d="M6 11l3.5 3.5L16 8" fill="none" stroke="var(--green)" stroke-width="2.4"/></svg>Personal protective equipment, cleaning supplies, and other health and safety measures.</li>
    <li><svg width="22" height="22" viewBox="0 0 22 22"><circle cx="11" cy="11" r="10" fill="none" stroke="var(--green)" stroke-width="2"/><path d="M6 11l3.5 3.5L16 8" fill="none" stroke="var(--green)" stroke-width="2.4"/></svg>Equipment and supplies used to respond to COVID-19.</li>
    <li><svg width="22" height="22" viewBox="0 0 22 22"><circle cx="11" cy="11" r="10" fill="none" stroke="var(--green)" stroke-width="2"/><path d="M6 11l3.5 3.5L16 8" fill="none" stroke="var(--green)" stroke-width="2.4"/></svg>Material goods (i.e., to facilitate play or safe sleep) or services (i.e., food) used for the operation of the program. Yes, Food is an allowable expense.</li>
    <li><svg width="22" height="22" viewBox="0 0 22 22"><circle cx="11" cy="11" r="10" fill="none" stroke="var(--green)" stroke-width="2"/><path d="M6 11l3.5 3.5L16 8" fill="none" stroke="var(--green)" stroke-width="2.4"/></svg>Mental health services for children and employees.</li>
  </ul>

  <section class="video-band">
    <p class="video-title">Check out our video <a href="https://www.pantryandgoodsdepot.com/video-resources/">click link here</a></p>
    <p class="video-url">https://www.pantryandgoodsdepot.com/video-resources/</p>
  </section>

  <section class="closing">
    <p>If you have not applied for the grant, we can help point you in the right direction.</p>
    <p>No purchase is necessary for this guidance, but we would love the opportunity to show you how we can stretch your purchases by <span class="green">up to 30%.</span></p>
  </section>

  <div class="contact-tab">CONTACT US</div>
  <footer class="contact-band">
    <ul class="contact-list">
      <li class="phone"><svg width="14" height="14" viewBox="0 0 24 24"><path d="M6.6 10.8a15 15 0 006.6 6.6l2.2-2.2a1 1 0 011-.25 11.4 11.4 0 003.6.6 1 1 0 011 1V20a1 1 0 01-1 1A17 17 0 013 4a1 1 0 011-1h3.5a1 1 0 011 1c0 1.25.2 2.45.6 3.6a1 1 0 01-.25 1z" fill="var(--green)"/></svg>877. 391.6052</li>
      <li><svg width="14" height="11" viewBox="0 0 14 11"><rect width="14" height="11" rx="1" fill="var(--green)"/><path d="M1 1l6 5 6-5" fill="none" stroke="var(--blue)" stroke-width="1.4"/></svg>stablization@pantryandgoodsdepot.com</li>
      <li><svg width="14" height="14" viewBox="0 0 14 14"><circle cx="7" cy="7" r="6" fill="none" stroke="var(--green)" stroke-width="1.6"/><path d="M1 7h12M7 1c-3 3.5-3 8.5 0 12M7 1c3 3.5 3 8.5 0 12" fill="none" stroke="var(--green)" stroke-width="1.2"/></svg>www.pantryandgoodsdepot.com</li>
    </ul>
    <div class="follow">FOLLOW US ON:
      <div class="social"><span></span><span></span><span></span></div>
    </div>
  </footer>
</main>
</body>
</html>
```